Real Estate Investment Company Needs Business Card Design

TurnKeyDeal9 is a real estate investment company that primarily deals directly with homeowners looking to sell their homes in "as is" condition as quick as possible. We give this seller cash and close on their nightmare of a property in just a matter of days.

Our logo is attached - (please keep logo in tact, use as is)

Industry/Entity Type

Real Estate

Contact Information for Business Card

The design should invoke trust & professionalism. The person holding the card should feel rest assured that we are the right company to work with.

Font styles to use
Sans Serif

Requirements
Must have
• Card must include "Call us today for a fair offer on your property so you can move on with your life!"
Nice to have
• If possible, include this either on front or back (you can use your own formatting, below is just the text)
• "
• No Realtor Commissions
• No Repairs To Deal With
• No Closing Costs "

```html
<!DOCTYPE html>
<html lang="en">
<head>
<meta charset="utf-8">
<title>TurnKeyDeal9 Business Card</title>
<link href="https://fonts.googleapis.com/css2?family=Source+Sans+3:wght@400;600&display=swap" rel="stylesheet">
<style>
  :root {
    --page: #e9e6e1;
    --card: #0b0b0c;
    --card-glow: #1c1d20;
    --brand-blue: #3f93d8;
    --title-blue: #2f5fa8;
    --contact-blue: #3a6fc0;
    --address: #c9c9c9;
    --silver: #c4c6c9;
    --tagline: #9a9ca0;
    --faint: #141517;
  }
  * { box-sizing: border-box; margin: 0; padding: 0; }
  html, body {
    width: 1200px;
    height: 900px;
    overflow: hidden;
    background: var(--page);
    font-family: "Source Sans 3", Arial, sans-serif;
  }
  .stage {
    width: 1200px;
    height: 900px;
    display: flex;
    flex-direction: column;
    align-items: center;
    justify-content: center;
    gap: 48px;
  }
  .card {
    position: relative;
    width: 630px;
    height: 360px;
    background: radial-gradient(ellipse at 55% 40%, var(--card-glow) 0%, var(--card) 70%);
    box-shadow: 0 10px 28px rgba(0,0,0,0.25);
    overflow: hidden;
  }
  .card-back {
    display: flex;
    flex-direction: column;
    align-items: center;
    justify-content: center;
    gap: 18px;
  }
  .card-back .brand-name {
    font-size: 48px;
    font-weight: 600;
    color: var(--silver);
  }
  .card-back .tagline {
    width: 420px;
    font-size: 15px;
    line-height: 1.4;
    text-align: center;
    color: var(--tagline);
  }
  .faint-mark {
    position: absolute;
    left: 30px;
    top: 40px;
    width: 210px;
    height: 210px;
    border-radius: 50%;
    background: var(--faint);
  }
  .front-brand {
    position: absolute;
    right: 40px;
    top: 42px;
    display: flex;
    align-items: center;
    gap: 10px;
  }
  .front-brand .dot {
    width: 16px;
    height: 16px;
    border-radius: 50%;
    background: var(--brand-blue);
  }
  .front-brand .brand-name {
    font-size: 32px;
    font-weight: 600;
    color: var(--brand-blue);
  }
  .holder {
    position: absolute;
    left: 48px;
    top: 150px;
  }
  .holder-name {
    font-size: 32px;
    color: var(--brand-blue);
    line-height: 1.1;
  }
  .holder-title {
    font-size: 17px;
    color: var(--title-blue);
  }
  .contact {
    position: absolute;
    left: 48px;
    top: 250px;
    font-size: 16px;
    line-height: 1.5;
  }
  .contact .address { color: var(--address); }
  .contact .line { color: var(--contact-blue); }
  .contact .line span { margin-right: 12px; }
</style>
</head>
<body>
<main class="stage">
  <section class="card card-back" aria-label="Card back">
    <span class="brand-name">TurnKeyDeal9</span>
    <p class="tagline">Call us today for a fair offer on your property so you can move on with your life!</p>
  </section>

  <section class="card card-front" aria-label="Card front">
    <div class="faint-mark" aria-hidden="true"></div>
    <div class="front-brand">
      <span class="dot" aria-hidden="true"></span>
      <span class="brand-name">TurnKeyDeal9</span>
    </div>
    <div class="holder">
      <p class="holder-name">Daniel Brooks</p>
      <p class="holder-title">Managing Director</p>
    </div>
    <div class="contact">
      <p class="address">1234, Address GoesHere, Country, 12345</p>
      <p class="line"><span>T: (044) 123 456 789</span><span>F: (044) 123456789</span><span>M: (044)123456789</span></p>
      <p class="line"><span>E: info@youremail.com</span><span>www.yourweb.com</span></p>
    </div>
  </section>
</main>
</body>
</html>
```